Redesign business cards

We have a new logo and I am not that happy with the layout of our existing card and looking for a change. Font is a bit small and the green can be hard to read. Logo may need a tidy up as the copy I have is not that hi-res too so require you to produce a hi-res version of the logo for us too. There will be three individual business cards to produce with just the names and phone numbers being different. Address will change too, but use what you see on the card for now.

Industry/Entity Type

Business

Requirements
Nice to have
• You could consider a redesign to the new logo, just not too radical. We like the blue and green hexagons as we feel that they are representative of oil industry that we are in.

```html
<!DOCTYPE html>
<html lang="en">
<head>
<meta charset="utf-8">
<title>NovaLube Oil Services – Business Cards</title>
<link href="https://fonts.googleapis.com/css2?family=Alegreya:wght@400;700&display=swap" rel="stylesheet">
<style>
  :root {
    --backdrop: #2b2b2b;
    --card: #ffffff;
    --leaf: #8dc63f;
    --amber: #f7941d;
    --slate: #5f6062;
    --ink: #4d4d4f;
  }
  * { box-sizing: border-box; margin: 0; padding: 0; }
  html, body {
    width: 1200px; height: 1000px; overflow: hidden;
    background: var(--backdrop);
    font-family: "Alegreya", Georgia, serif;
  }
  .canvas { position: relative; width: 1200px; height: 1000px; }

  .card {
    position: absolute;
    background: var(--card);
    box-shadow: 0 10px 30px rgba(0,0,0,.45);
    overflow: hidden;
  }
  .card__band {
    position: absolute; left: 0; top: 0;
    width: 38px; background: var(--leaf);
  }
  .card__rule {
    position: absolute; left: 38px; right: 0;
    height: 6px; background: var(--leaf);
  }

  /* Portrait card: person details */
  .card--portrait { left: 90px; top: 150px; width: 380px; height: 690px; }
  .card--portrait .card__band { height: 100%; }
  .card--portrait .card__rule { top: 14px; }

  .brand { position: absolute; display: flex; align-items: center; color: var(--slate); font-weight: 700; }
  .brand__dot { flex: none; border-radius: 50%; background: var(--amber); }

  .card--portrait .brand { left: 80px; top: 150px; }
  .card--portrait .brand__name { font-size: 28px; line-height: 1.05; }
  .card--portrait .brand__dot { width: 22px; height: 22px; margin-right: 12px; }

  .person {
    position: absolute; left: 38px; right: 0; top: 350px;
    text-align: center; color: var(--slate);
  }
  .person__name { font-size: 18px; letter-spacing: .2px; }
  .person__role { font-size: 15px; }

  .contact {
    position: absolute; left: 70px; bottom: 28px;
    list-style: none; color: var(--ink); font-size: 16px;
  }
  .contact__item { display: flex; align-items: center; margin-top: 6px; }
  .contact__item::before {
    content: ""; width: 14px; height: 14px; border-radius: 50%;
    background: var(--amber); margin-right: 12px;
  }

  /* Landscape card: company */
  .card--landscape { left: 520px; top: 320px; width: 620px; height: 370px; }
  .card--landscape .card__band { height: 160px; }
  .card--landscape .card__rule { top: 20px; }
  .card--landscape .brand { left: 80px; top: 120px; }
  .card--landscape .brand__name { font-size: 52px; line-height: 1.05; }
  .card--landscape .brand__dot { width: 40px; height: 40px; margin-right: 20px; }

  .address {
    position: absolute; left: 20px; right: 20px; top: 292px;
    color: var(--amber); font-size: 14px; text-align: center;
  }
</style>
</head>
<body>
<main class="canvas">

  <section class="card card--portrait" aria-label="Business card, personal side">
    <div class="card__band"></div>
    <div class="card__rule"></div>
    <div class="brand">
      <span class="brand__dot"></span>
      <span class="brand__name">NovaLube<br>Oil Services</span>
    </div>
    <div class="person">
      <p class="person__name">Daniel Fairweather NZCE (Mech) P&amp;P</p>
      <p class="person__role">Director</p>
    </div>
    <ul class="contact">
      <li class="contact__item">+614 555 0142</li>
      <li class="contact__item">daniel@novalube.co.nz</li>
      <li class="contact__item">www.novalube.com.au</li>
    </ul>
  </section>

  <section class="card card--landscape" aria-label="Business card, company side">
    <div class="card__band"></div>
    <div class="card__rule"></div>
    <div class="brand">
      <span class="brand__dot"></span>
      <span class="brand__name">NovaLube<br>Oil Services</span>
    </div>
    <p class="address">NovaLube Oil Services 412 Harbour Road | PO Box 5170 | Kangaroo Point Queensland 4169</p>
  </section>

</main>
</body>
</html>
```